Brimovex business card

Based on company logo and website given , to design a business card temple. Slogan "Your furry friends deserves the best"
Color style please refer to our website

```html
<!DOCTYPE html>
<html lang="en">
<head>
<meta charset="utf-8">
<title>Brimovex business card</title>
<link rel="stylesheet" href="https://fonts.googleapis.com/css2?family=Merriweather:wght@400;700;900&display=swap">
<style>
  :root {
    --stage: #1d1d1d;
    --forest: #123d37;
    --forest-deep: #0c2c28;
    --sun: #f6d312;
    --mist: #edf3f5;
    --ink: #151515;
    --slogan: #9fb2ad;
    --pet-light: #e3cfa8;
    --pet-dark: #8a7258;
  }
  * { margin: 0; padding: 0; box-sizing: border-box; }
  html, body { width: 1200px; height: 876px; overflow: hidden; }
  body {
    background: var(--stage);
    font-family: "Merriweather", Georgia, serif;
    position: relative;
  }
  .card {
    position: absolute;
    top: 279px;
    width: 520px;
    height: 318px;
    border-radius: 4px;
    overflow: hidden;
    box-shadow: 0 18px 40px rgba(0,0,0,.55);
  }
  .card--front {
    left: 60px;
    background: radial-gradient(ellipse at 35% 30%, var(--forest) 0%, var(--forest-deep) 100%);
  }
  .front-brand {
    position: absolute;
    left: 0; right: 0;
    top: 168px;
    text-align: center;
  }
  .front-brand__name {
    color: var(--sun);
    font-weight: 900;
    font-size: 44px;
    letter-spacing: .5px;
    line-height: 1;
  }
  .front-brand__slogan {
    margin-top: 10px;
    color: var(--slogan);
    font-size: 15px;
    font-weight: 400;
  }

  .card--back {
    left: 620px;
    background: var(--mist);
  }
  .back-sun {
    position: absolute;
    left: 268px;
    top: 66px;
    width: 210px;
    height: 210px;
    border-radius: 50%;
    background: var(--sun);
  }
  .back-pets {
    position: absolute;
    left: 220px;
    top: 150px;
    width: 300px;
    height: 168px;
    border-top-left-radius: 90px;
    background: linear-gradient(100deg, var(--pet-dark) 0%, #b79f7c 40%, var(--pet-light) 75%, #d8c39c 100%);
    opacity: .95;
  }
  .back-brand {
    position: absolute;
    left: 30px;
    top: 26px;
    color: var(--ink);
    font-weight: 900;
    font-size: 32px;
    line-height: 1;
  }
  .contact {
    position: absolute;
    left: 30px;
    top: 84px;
    list-style: none;
    color: var(--ink);
    font-size: 12px;
    line-height: 1.45;
  }
  .contact__item {
    display: flex;
    gap: 8px;
    margin-bottom: 8px;
  }
  .contact__icon {
    flex: none;
    width: 15px;
    height: 15px;
    margin-top: 1px;
  }
</style>
</head>
<body>

<section class="card card--front">
  <div class="front-brand">
    <p class="front-brand__name">Brimovex</p>
    <p class="front-brand__slogan">Your furry friends deserves the best</p>
  </div>
</section>

<section class="card card--back">
  <div class="back-sun"></div>
  <div class="back-pets" role="img" aria-label="Photo of a kitten and a labrador puppy facing each other"></div>

  <p class="back-brand">Brimovex</p>

  <ul class="contact">
    <li class="contact__item">
      <svg class="contact__icon" viewBox="0 0 16 16" aria-hidden="true">
        <circle cx="8" cy="8" r="8" fill="#f6d312"/>
        <path d="M5.2 4.2l1.4-.3.8 1.9-.9.7a5 5 0 0 0 2.9 2.9l.7-.9 1.9.8-.3 1.4c-3.6.2-6.7-2.9-6.5-6.5z" fill="#151515"/>
      </svg>
      <span>+61 3 9047 2261<br>1800 604 318</span>
    </li>
    <li class="contact__item">
      <svg class="contact__icon" viewBox="0 0 16 16" aria-hidden="true">
        <circle cx="8" cy="8" r="8" fill="#f6d312"/>
        <rect x="4.3" y="5.3" width="7.4" height="5.4" rx=".6" fill="#151515"/>
        <path d="M4.6 5.7L8 8.3l3.4-2.6" stroke="#f6d312" stroke-width=".8" fill="none"/>
      </svg>
      <span>www.brimovex.com.au<br>sales@brimovex.com.au</span>
    </li>
    <li class="contact__item">
      <svg class="contact__icon" viewBox="0 0 16 16" aria-hidden="true">
        <circle cx="8" cy="8" r="8" fill="#f6d312"/>
        <path d="M8 3.6a2.9 2.9 0 0 0-2.9 2.9C5.1 8.8 8 12.4 8 12.4s2.9-3.6 2.9-5.9A2.9 2.9 0 0 0 8 3.6z" fill="#151515"/>
        <circle cx="8" cy="6.5" r="1.1" fill="#f6d312"/>
      </svg>
      <span>4/22 Darnell Street<br>Glen Ashby Vic 3152</span>
    </li>
  </ul>
</section>

</body>
</html>
```